Nutrigenomics Business card design

Nutrigenomics is an exciting emerging field where I sequence the DNA from a saliva swab and then tailor a personalised nutritional program according to the persons genetics. It is possible to turn down undesirable genes that may be stuck "on" all the time causing inflammation etc. Equally important we switch "on" genes that might be stuck "off" as is often the case with autism. A large portion of my clients are autistic children. We see huge changes in functionality with the appropriate changes in diet to regulate their gene expression. This technology is definitely the way of the future.
I need a logo that will clearly show the combination of genetics with nutrition. The word "Nutrigenomics" still isn't in common use yet. I'm thinking maybe a DNA helix - (I think most people associate a helix with DNA or genes, but I'm open to suggestions) Combined somehow with food - preferably vegetables/ fruit/ meat/eggs etc. Definitely not grains or dairy - we take autistic kids off those 2 food groups straight away.
Green in it somewhere? I somehow associates healthy living / whole foods nutrition with the colour green. You guys know more about colours than me :-)
Maybe a helix could morph into a body shape filled with foods (along the lines of "you are what you eat" or something...)

Target Market(s)

The majority of my clients to date are people in their 40's wanting to improve their health or their children's health.

Industry/Entity Type

Nutrition

Contact Information for Business Card

Front of card:
Dr Moira Crandle (B App Sci, PhD Molecular Pathology)
Certified Vitalorin Practitioner and LUMO Nutritionist
247 Pellbrook Rd, Pellbrook
0417836254
dr.moiracrandle@examplemail.com.au
drmoiracrandle.com.au
Back of card:
Small Photo of me, Dr Moira Crandle
Specialises in Autism, ADHD, Fussy Eaters, Gut Issues, Food Intolerances, Healthy Ageing

Logo Text

Dr Moira Crandle

Logo styles of interest
Pictorial/Combination Logo
Character Logo
Requirements
Must have
• A logo showing a clear link between genes and nutrition
The box for what I want written on the card is not coming up when I try to edit so I'll put it here....
Front of card:
Dr Moira Crandle
(B App Sci, PhD Molecular Pathology) in smaller writing under my name

Certified Nutrigenomist
Certified LUMO Nutritionist

then use your nice symbols for the address, ph etc as below

247 Pellbrook Rd, Pellbrook
0417836254
dr.moiracrandle@examplemail.com.au
www.drmoiracrandle.com.au

Back of card:
Small Photo of me
Dr Moira Crandle
Specialises in:
Nutrigenomics
Healthy Ageing
Autism / ADHD
Gut Issues
Food Intolerances
Should not have
• No bread or grains of any sort
No dairy - milk cheese etc

```html
<!DOCTYPE html>
<html lang="en">
<head>
<meta charset="utf-8">
<title>Dr Moira Crandle – Business Card</title>
<link href="https://fonts.googleapis.com/css2?family=Roboto:wght@300;400&display=swap" rel="stylesheet">
<style>
  :root {
    --backdrop: #000000;
    --card-grey: #d3d5d2;
    --card-white: #ffffff;
    --leaf-green: #a6c13f;
    --name-green: #6fa636;
    --ink: #3c3c3c;
    --ink-soft: #555555;
    --on-green: #ffffff;
  }
  * { margin: 0; padding: 0; box-sizing: border-box; }
  html, body {
    width: 1200px; height: 849px; overflow: hidden;
    background: var(--backdrop);
    font-family: "Roboto", Helvetica, Arial, sans-serif;
    font-weight: 300;
  }
  .stage {
    position: absolute; left: 0; top: 0;
    width: 1171px; height: 828px;
    transform: scale(1.0248, 1.0254);
    transform-origin: 0 0;
  }
  .card {
    position: absolute; top: 314px;
    width: 349px; height: 199px;
    border-radius: 9px; overflow: hidden;
    background: var(--card-grey);
  }
  .card--front { left: 223px; }
  .card--back { left: 618px; }
  .card__wave { position: absolute; inset: 0; width: 100%; height: 100%; }
  .card__text { position: absolute; white-space: nowrap; line-height: 1; }

  /* front */
  .emblem {
    position: absolute; left: 8px; top: 28px; width: 152px; height: 130px;
    border-radius: 40% 40% 30% 30%;
    background: radial-gradient(ellipse at 50% 40%, #c96a3a 0%, #8fae3d 45%, rgba(90,160,60,0.55) 70%, rgba(211,213,210,0) 100%);
  }
  .front__name { left: 170px; top: 23px; font-size: 20px; color: var(--name-green); }
  .front__degrees { left: 170px; top: 52px; font-size: 8.4px; color: var(--ink); }
  .front__cert { left: 170px; font-size: 10px; color: var(--ink); }
  .front__cert--one { top: 74px; }
  .front__cert--two { top: 86px; }
  .contact { position: absolute; left: 172px; display: flex; align-items: center; gap: 8px; font-size: 10.2px; color: var(--ink); white-space: nowrap; }
  .contact svg { width: 9px; height: 9px; flex: none; }
  .contact--address { top: 121px; }
  .contact--phone { top: 133px; }
  .contact--email { top: 145px; font-size: 8.6px; }
  .contact--web { top: 158px; }

  /* back */
  .portrait {
    position: absolute; left: 66px; top: 35px; width: 60px; height: 79px;
    border-radius: 5px;
    background: linear-gradient(160deg, #4a2a20 0%, #8a5a44 45%, #d8a98c 70%, #5a3526 100%);
  }
  .back__name { left: 175px; top: 35px; font-size: 18px; color: var(--on-green); }
  .specialties { position: absolute; left: 175px; top: 65px; list-style: none; font-size: 11px; color: var(--on-green); line-height: 14px; }
  .specialties li::before { content: "• "; }
</style>
</head>
<body>
<main class="stage">
  <section class="card card--front" aria-label="Business card front">
    <svg class="card__wave" viewBox="0 0 349 199" preserveAspectRatio="none" aria-hidden="true">
      <path d="M107,0 C150,22 172,70 150,108 C125,150 40,150 0,193 L0,199 L349,199 L349,0 Z" fill="var(--card-white)"/>
    </svg>
    <div class="emblem" role="img" aria-label="Logo illustration: a DNA helix rising into a human figure filled with vegetables, fruit and eggs"></div>
    <p class="card__text front__name">Dr Moira Crandle</p>
    <p class="card__text front__degrees">(B App Sci, PhD Molecular Pathology)</p>
    <p class="card__text front__cert front__cert--one">Certified Nutrigenomist</p>
    <p class="card__text front__cert front__cert--two">Certified LUMO Nutritionist</p>
    <p class="contact contact--address">
      <svg viewBox="0 0 10 10" aria-hidden="true"><rect x="0.5" y="2" width="9" height="6.5" fill="#333"/><path d="M0.8,2.3 L5,5.6 L9.2,2.3" stroke="#fff" stroke-width="0.9" fill="none"/></svg>
      247 Pellbrook Rd, Pellbrook</p>
    <p class="contact contact--phone">
      <svg viewBox="0 0 10 10" aria-hidden="true"><path d="M2,1 L4,1 L4.6,3.4 L3.4,4.2 C4,5.6 4.6,6.2 5.8,6.8 L6.6,5.6 L9,6.2 L9,8.2 C5,9 1,5 2,1 Z" fill="#333"/></svg>
      0417836254</p>
    <p class="contact contact--email">
      <svg viewBox="0 0 10 10" aria-hidden="true"><rect x="0.5" y="1.5" width="9" height="7" rx="1" fill="#333"/><circle cx="5" cy="5" r="1.8" fill="#fff"/></svg>
      dr.moiracrandle@examplemail.com.au</p>
    <p class="contact contact--web">
      <svg viewBox="0 0 10 10" aria-hidden="true"><circle cx="5" cy="5" r="4.3" fill="#333"/><path d="M0.8,5 H9.2 M5,0.8 C3,3 3,7 5,9.2 M5,0.8 C7,3 7,7 5,9.2" stroke="#fff" stroke-width="0.7" fill="none"/></svg>
      www.drmoiracrandle.com.au</p>
  </section>

  <section class="card card--back" aria-label="Business card back">
    <svg class="card__wave" viewBox="0 0 349 199" preserveAspectRatio="none" aria-hidden="true">
      <path d="M100,0 C145,22 165,70 145,108 C120,150 40,150 0,193 L0,199 L349,199 L349,0 Z" fill="var(--leaf-green)"/>
    </svg>
    <div class="portrait" role="img" aria-label="Small portrait photo of Dr Moira Crandle"></div>
    <p class="card__text back__name">Dr Moira Crandle</p>
    <ul class="specialties">
      <li style="list-style:none" class="specialties__heading">Specialises in:</li>
      <li>Nutrigenomics</li>
      <li>Healthy Ageing</li>
      <li>Autism / ADHD</li>
      <li>Gut Issues</li>
      <li>Food Intolerances</li>
    </ul>
  </section>
</main>
<style>.specialties__heading::before{content:none !important;}</style>
</body>
</html>
```